Veltrane Partners Inc. - Cyber security company needs web site redesign

Need to redesign the corporate web page. Static content with no rss feeds. Web page is for basic marketing and corporate information. VPI is a management and cyber security consulting firm. The company logo has been redesigned and would like to incorporate this new logo into the design. Also need to reference MADE IN USA logo, SDVOSB logo, Include the current content from the existing web page and will revise as needed
Updates

Target Market(s)

Government and Commercial Clients and potential new employees

Industry/Entity Type

It Company

Number of Pages Required

1 page

Font styles to use
Sans Serif

Requirements
Must have
• New Veltrane Partners Logo
• MADE IN USA logo
• SDVOSB logo
• Cyber security theme
Nice to have
• animation
• Cyber security related graphics
Should not have
• Search and News sections

```html
<!DOCTYPE html>
<html lang="en">
<head>
<meta charset="utf-8">
<title>Veltrane Partners Inc.</title>
<link href="https://fonts.googleapis.com/css2?family=Open+Sans:wght@400;600;700&display=swap" rel="stylesheet">
<style>
:root{
  --red:#d9201f;
  --navy:#1d4f9c;
  --blue:#1a56b0;
  --ink:#2b2b2b;
  --muted:#777;
  --footer:#1b1b1b;
}
*{margin:0;padding:0;box-sizing:border-box}
html,body{width:1200px;height:2612px;overflow:hidden}
body{font-family:"Open Sans",Arial,sans-serif;color:var(--ink);background:#fff;position:relative}
.abs{position:absolute}
/* header */
.top{left:0;top:0;width:1200px;height:160px;background:#fff}
.brand{left:30px;top:50px;display:flex;align-items:center;gap:14px}
.brand-mark{width:44px;height:44px;background:var(--red)}
.brand-name{font-size:26px;font-weight:700;color:var(--red)}
.phone{left:720px;top:96px;display:flex;align-items:center;gap:14px;font-size:30px;font-weight:600;color:#333}
.login{left:1000px;top:88px;width:102px;height:50px;background:var(--red);color:#fff;font-size:18px;font-weight:600;display:flex;align-items:center;justify-content:center;gap:8px}
.nav{left:0;top:170px;width:1200px;height:50px;background:#222}
.nav ul{list-style:none;display:flex;margin-left:100px;height:50px}
.nav li{width:110px;text-align:center;line-height:50px;color:#eee;font-size:16px}
.nav li.active{background:var(--red);color:#fff}
/* hero */
.hero{left:0;top:220px;width:1200px;height:600px;background:linear-gradient(160deg,#2d3238 0%,#17191c 45%,#3a3e44 70%,#101214 100%)}
.hero h1{position:absolute;left:0;width:1200px;top:290px;text-align:center;font-size:58px;font-weight:700;color:#fff;letter-spacing:1px}
.hero h1 span{color:var(--blue)}
.hero p{position:absolute;left:0;width:1200px;top:370px;text-align:center;color:#ddd;font-size:16px;line-height:24px}
.btn{display:inline-block;background:var(--navy);color:#fff;font-size:15px;font-weight:600;width:100px;height:36px;line-height:36px;text-align:center;border-radius:2px}
.hero .btn{position:absolute;left:550px;top:462px}
/* content blocks */
.kicker{font-size:18px;color:var(--red);font-weight:600}
.title{font-size:46px;color:#333;font-weight:400;line-height:54px}
.title.sub{font-size:34px;line-height:42px}
.bar{border-left:4px solid var(--red);padding-left:14px}
.body{font-size:15px;line-height:24px;color:var(--muted)}
.lead{font-size:18px;line-height:26px;color:#4a5b78;font-weight:600}
.intro{left:100px;top:905px;width:560px}
.intro .body{margin:28px 0 34px}
.locks{left:740px;top:912px;width:360px;height:250px;background:linear-gradient(135deg,#0b1a2e,#123456 60%,#0a1524)}
.band-grey{left:0;top:1280px;width:1200px;height:340px;background:linear-gradient(90deg,#e9e9e9,#f6f6f6)}
.laptop{left:0;top:1280px;width:560px;height:340px;background:linear-gradient(135deg,#9aa3ad,#d7dbe0 50%,#6c7580)}
.benefit{left:596px;top:1300px;width:520px}
.benefit .lead,.career .lead{margin:16px 0 16px}
.benefit .body,.career .body{margin-bottom:26px}
.career{left:100px;top:1650px;width:520px}
.cloud{left:650px;top:1620px;width:550px;height:340px;background:linear-gradient(120deg,#ffffff 0%,#dde6ef 40%,#a9bccf 100%)}
/* services */
.services{left:0;top:1960px;width:1200px;height:320px;background:linear-gradient(180deg,#1b56b4,#123f8a)}
.services h2{position:absolute;top:46px;width:1200px;text-align:center;font-size:28px;font-weight:600;color:#fff}
.services h2::before{content:"";display:inline-block;width:8px;height:8px;background:var(--red);margin-right:10px;vertical-align:middle}
.svc{position:absolute;top:130px;width:200px;text-align:center;color:#fff}
.svc .ic{width:88px;height:88px;border-radius:50%;background:#fff;margin:0 auto 14px;display:flex;align-items:center;justify-content:center}
.svc h3{font-size:15px;font-weight:600}
.svc p{font-size:13px;line-height:19px;color:#cfdcf2;margin-top:4px}
/* footer */
.footer{left:0;top:2280px;width:1200px;height:300px;background:var(--footer)}
.foot-col h4{font-size:16px;font-weight:600;color:#eee;margin-bottom:16px}
.quick-links{left:100px;top:2310px}
.links{list-style:none}
.links li{font-size:14px;line-height:25px;color:#bbb}
.links li::before{content:"› ";color:var(--red)}
.inquiry{left:316px;top:2310px;width:200px}
.field{background:#fff;height:30px;margin-bottom:10px;color:#999;font-size:13px;padding:6px 10px}
.field.tall{height:44px}
.submit{background:var(--red);color:#fff;font-size:13px;font-weight:700;width:80px;height:28px;line-height:28px;text-align:center}
.contact{left:612px;top:2310px;width:300px}
.contact .row{display:flex;gap:14px;align-items:flex-start;font-size:13px;line-height:19px;color:#bbb;margin-bottom:18px}
.contact svg{flex:none}
.foot-brand{left:930px;top:2410px;width:240px;font-size:20px;font-weight:700;color:#555;white-space:nowrap}
.copy{left:0;top:2580px;width:1200px;height:32px;background:#0c0c0c;color:#aaa;font-size:13px;text-align:center;line-height:32px}
</style>
</head>
<body>
<header class="abs top">
  <div class="abs brand"><span class="brand-mark"></span><span class="brand-name">Veltrane Partners Inc.</span></div>
  <div class="abs phone">
    <svg width="34" height="34" viewBox="0 0 34 34"><circle cx="17" cy="17" r="16" fill="var(--navy)"/><path d="M11 9l4 1 1 5-3 2c1 3 3 5 6 6l2-3 5 1 1 4c-1 2-3 3-5 2-7-2-12-7-14-14-1-2 1-4 3-4z" fill="#fff"/></svg>
    (555) 014-2270
  </div>
  <div class="abs login"><svg width="14" height="14" viewBox="0 0 14 14"><rect x="2" y="6" width="10" height="8" fill="#fff"/><path d="M4 6V4a3 3 0 016 0v2" stroke="#fff" stroke-width="2" fill="none"/></svg>Login</div>
</header>
<nav class="abs nav"><ul><li class="active">Home</li><li>Services</li><li>About Us</li><li>Careers</li><li>Contact Us</li></ul></nav>

<section class="abs hero" role="img" aria-label="Photo of a person in a white shirt holding a tablet over dark binary code">
  <h1>WELCOME TO <span>SDVOSB</span></h1>
  <p>Lorem ipsum dolor sit amet, consectetur adipiscing elit, sed do eiusmod<br>tempor incididunt ut labore et dolore.</p>
  <span class="btn">Read More</span>
</section>

<section class="abs intro">
  <div class="bar"><div class="kicker">Welcome To</div><div class="title">SDVOSB</div></div>
  <p class="body">Lorem ipsum dolor sit amet, consectetur adipiscing elit, sed do eiusmod tempor incididunt ut labore et dolore magna aliqua. Ut enim ad minim veniam, quis nostrud exercitation ullamco laboris nisi ut aliquip ex ea commodo consequat. Duis aute irure dolor in reprehenderit in voluptate velit esse cillum dolore eu fugiat nulla pariatur. Excepteur sint occaecat cupidatat non proident, sunt in culpa qui officia deserunt.</p>
  <span class="btn">Read More</span>
</section>
<div class="abs locks" role="img" aria-label="Glowing blue padlocks with one open red padlock"></div>

<div class="abs band-grey"></div>
<div class="abs laptop" role="img" aria-label="Hands typing on a laptop keyboard"></div>
<section class="abs benefit">
  <div class="bar"><div class="title sub">Benefit Package</div></div>
  <p class="lead">Sed ut perspiciatis unde omnis iste natus error sit voluptatem accusantium doloremque laudantium</p>
  <p class="body">Lorem ipsum dolor sit amet, consectetur adipiscing elit, sed do eiusmod tempor incididunt ut labore et dolore magna aliqua. Ut enim ad minim veniam, quis nostrud exercitation ullamco laboris nisi ut aliquip ex ea commodo consequat. Duis aute irure dolor in reprehenderit.</p>
  <span class="btn">Read More</span>
</section>

<div class="abs cloud" role="img" aria-label="Cloud outline with a padlock over a field of numbers"></div>
<section class="abs career">
  <div class="bar"><div class="title sub">Career</div></div>
  <p class="lead">Sed ut perspiciatis unde omnis iste natus error sit voluptatem accusantium doloremque laudantium</p>
  <p class="body">Lorem ipsum dolor sit amet, consectetur adipiscing elit, sed do eiusmod tempor incididunt ut labore et dolore magna aliqua. Ut enim ad minim veniam, quis nostrud exercitation ullamco laboris nisi ut aliquip ex ea commodo consequat. Duis aute irure dolor in reprehenderit.</p>
  <span class="btn">Read More</span>
</section>

<section class="abs services">
  <h2>Our Services</h2>
  <div class="svc" style="left:90px"><div class="ic"><svg width="44" height="44" viewBox="0 0 44 44"><circle cx="22" cy="22" r="18" fill="none" stroke="var(--red)" stroke-width="4"/><path d="M22 22V4a18 18 0 0118 18z" fill="var(--red)"/></svg></div><h3>Threat Analysis</h3><p>Lorem ipsum dolor sit amet,<br>consectetur adipiscing</p></div>
  <div class="svc" style="left:290px"><div class="ic"><svg width="44" height="44" viewBox="0 0 44 44"><path d="M22 4l15 6v10c0 10-7 17-15 20C14 37 7 30 7 20V10z" fill="var(--red)"/><path d="M15 22l5 5 10-10" stroke="#fff" stroke-width="4" fill="none"/></svg></div><h3>Threat Mitigation</h3><p>Lorem ipsum dolor sit amet,<br>consectetur adipiscing</p></div>
  <div class="svc" style="left:500px"><div class="ic"><svg width="44" height="44" viewBox="0 0 44 44"><circle cx="22" cy="18" r="12" fill="var(--red)"/><rect x="16" y="31" width="12" height="8" fill="var(--red)"/></svg></div><h3>Automation Solutions</h3><p>Lorem ipsum dolor sit amet,<br>consectetur adipiscing</p></div>
  <div class="svc" style="left:710px"><div class="ic"><svg width="44" height="44" viewBox="0 0 44 44"><circle cx="19" cy="19" r="12" fill="none" stroke="var(--red)" stroke-width="5"/><path d="M28 28l10 10" stroke="var(--red)" stroke-width="6"/></svg></div><h3>Malware Analysis</h3><p>Lorem ipsum dolor sit amet,<br>consectetur adipiscing</p></div>
  <div class="svc" style="left:910px"><div class="ic"><svg width="44" height="44" viewBox="0 0 44 44"><circle cx="22" cy="22" r="9" fill="none" stroke="var(--red)" stroke-width="6"/><path d="M22 4v8M22 32v8M4 22h8M32 22h8M9 9l6 6M29 29l6 6M35 9l-6 6M15 29l-6 6" stroke="var(--red)" stroke-width="5"/></svg></div><h3>Threat Operations</h3><p>Lorem ipsum dolor sit amet,<br>consectetur adipiscing</p></div>
</section>

<footer class="abs footer"></footer>
<div class="abs foot-col quick-links"><h4>Quick Links</h4>
  <ul class="links"><li>Home</li><li>Services</li><li>About Us</li><li>Careers</li><li>Contact Us</li></ul></div>
<div class="abs foot-col inquiry"><h4>Quick Inquiry</h4>
  <div class="field">Name</div><div class="field">Email</div><div class="field tall">Message</div><div class="submit">SUBMIT</div></div>
<div class="abs foot-col contact"><h4>Contact Details</h4>
  <div class="row"><svg width="16" height="20" viewBox="0 0 16 20"><path d="M8 0a7 7 0 017 7c0 5-7 13-7 13S1 12 1 7a7 7 0 017-7z" fill="#ddd"/><circle cx="8" cy="7" r="3" fill="#1b1b1b"/></svg><span>4820 Harbor Mill Road #210<br>Lakeport NY 14000</span></div>
  <div class="row"><svg width="16" height="16" viewBox="0 0 16 16"><path d="M3 1l3 1 1 3-2 1c1 2 3 4 5 5l1-2 3 1 1 3c-1 2-3 2-5 1C6 12 3 9 2 5 1 3 1 1 3 1z" fill="#ddd"/></svg><span>(555) 014-2270</span></div>
  <div class="row"><svg width="18" height="14" viewBox="0 0 18 14"><rect width="18" height="14" fill="#ddd"/><path d="M0 0l9 7 9-7" stroke="#1b1b1b" stroke-width="1.5" fill="none"/></svg><span>info@veltranepartners.com</span></div>
</div>
<div class="abs foot-brand">Veltrane Partners Inc.</div>
<div class="abs copy">Copyright 2014 All rights reserved</div>
</body>
</html>
```